Falzflyer - Netzwerkwartung
Zielgruppe
IT-Firmenkunden im Netzwerkbereich. Firmengrössen 1-100 Mitarbeiter. Privat Kunden, aber das hat mit diesem Flyer dann nichts zu tun. Der Flyer richtet sich ausschliesslich an Firmenkunden.
Aufgabenstellung
Falzflyer, Endfassung gefaltet DIN A5 (148 x 210 mm) hoch, Wickelfalz.
Offenes Endformat: 442 x 210 mm
Datenformat: 446 x 214 mm
Wir haben bereits einige bestehende doppelseitige Flyer (s. Beilagen) – der neue Flyer soll einen ähnlichen Look entsprechen damit eine leichte Wiedererkennung erfolgen kann. Allerdings wird es ein Falzflyer 3x gefalzt. Das zugeklappte Format ist schlussendlich A5. Wir lassen uns aber auch gerne belehren – falls das Design für diese Art von Flyer ungeeignet sein sollte. (kein Booklet)
Farben: Bordeaux – oder Ihr Farb-Vorschlag (anstelle grün, blau oder rot), jedoch nicht so dominant. Mehr weiss denn farbig.
Verfeinerung mit Symbolbildern oder Symbolen erwünscht.
Vorlage der Druckerei ist zu beachten – S. Anlagen in div. Formaten.
Standardfont ist immer Century Cothic.
Evtl. Infoboxen? Halt je nach Platz.
Fusszeile evtl. ausnutzen:
• Evtl. Schlagworte bezogen auf Inhalt
• Firmenname
• Telefon
• URL
• Unser Slogan WIR HABEN DIE LÖSUNG (muss!)
Unser Logo soll vorne gross (mit Swift Relay) und allenfalls noch am Ende etwas kleiner zusammen mit unseren Kontaktdaten zu finden sein. Für das Design des Wortes «Swift Relay» lassen wir uns gerne von Ihnen überraschen.
In der Anlage erhalten Sie die Inhalte als PUB Datei. Der Wortlaut darf nicht verändert werden. Bei Darstellung und Design sind Sie frei. Die Orange hervorgehobenen Texte sind das was wir anbieten. Der schwarze Text ist die Problembeschreibung. Evtl. haben Sie eine Idee wie das hervorgehoben werden kann – Kasten? Die Seiten sollen dann der Reihenfolge mit den Seiten im Flyer entsprechen. Gemäss Druckanweisung/Vorlage. Rot hervorgehobene Texte weglassen.
Unsere korrekten Kontaktdaten:
rechnerhannes.ch GmbH
9347 Lindenmatt + 8612 Tannegg
Telefon: 071 483 27 96
E-Mail: info@rechnerhannes.ch
Web: rechnerhannes.ch

```html
<!DOCTYPE html>
<html lang="de">
<head>
<meta charset="utf-8">
<title>Falzflyer Netzwerkwartung – rechnerhannes.ch</title>
<link rel="stylesheet" href="https://fonts.googleapis.com/css2?family=Didact+Gothic&family=Exo+2:wght@600;700&display=swap">
<style>
:root{
  --page:#c4c4c4;
  --paper:#f4f4f4;
  --paper-mid:#e6e6e6;
  --blue:#1fa6dc;
  --blue-deep:#1592cc;
  --blue-light:#45c3f0;
  --red:#a5181d;
  --heading:#b5262b;
  --ink:#2a2a2a;
  --green:#5aa332;
  --white:#ffffff;
}
*{box-sizing:border-box;margin:0;padding:0}
html,body{width:1200px;height:1199px;overflow:hidden;background:var(--page)}
body{position:relative;font-family:"Didact Gothic",sans-serif;color:var(--ink)}
.spread{position:absolute;left:30px;width:1140px;height:545px;display:grid;grid-template-columns:repeat(3,1fr);box-shadow:0 6px 14px rgba(0,0,0,.25)}
.spread--outside{top:40px}
.spread--inside{top:615px}
.panel{position:relative;background:var(--paper);border-top:8px solid var(--blue);padding:26px 26px 0;overflow:hidden}
.panel--shade{background:linear-gradient(90deg,#ececec,#f6f6f6 40%,#ececec)}
.panel__footer{position:absolute;left:0;right:0;bottom:0;height:38px;background:var(--red);display:flex;align-items:center;justify-content:center}
.footer-url{color:var(--blue-light);font-size:21px;letter-spacing:.3px}
.footer-slogan{color:var(--white);font-size:21px;letter-spacing:.5px}
h2{font-family:"Exo 2",sans-serif;font-weight:700;color:var(--heading);font-size:25px;line-height:1.1;margin-bottom:12px}
.section + .section{margin-top:30px}
p,li{font-size:9.4px;line-height:1.38}
p + p{margin-top:9px}
.lead{font-weight:bold;font-family:"Exo 2",sans-serif;font-weight:600;font-size:9.2px}
ul{list-style:none;margin:10px 0}
li{padding-left:8px;position:relative}
li::before{content:"•";position:absolute;left:0}
.infobox{background:var(--blue);color:var(--white);padding:12px 14px;margin-top:14px}
.infobox .lead{color:var(--white)}
.contact{position:absolute;left:26px;right:26px;bottom:0;height:92px;background:var(--red);color:var(--white);padding:10px 22px}
.contact h3{font-family:"Exo 2",sans-serif;font-weight:600;font-size:16px;text-align:center;margin-bottom:8px}
.contact__cols{display:flex;justify-content:space-between;font-size:9.2px;line-height:1.35}
/* cover */
.panel--cover{padding:0}
.cover__portrait{position:absolute;left:0;top:10px;width:168px;height:225px;background:radial-gradient(ellipse at 50% 40%,#e7d6cc,#b96a5a 55%,#6e2a28);border-radius:40% 40% 0 0}
.brand{position:absolute;left:178px;top:40px;width:190px;display:flex;align-items:center;gap:8px}
.brand__mark{width:26px;height:26px;background:var(--red);flex:none}
.brand__name{font-family:"Exo 2",sans-serif;font-weight:700;font-size:21px;line-height:1.05;color:var(--ink);letter-spacing:.5px}
.brand__tagline{position:absolute;left:212px;top:106px;font-family:"Exo 2",sans-serif;font-weight:600;font-size:15px;color:var(--green)}
.cover__swoosh{position:absolute;left:0;top:160px;width:380px;height:120px}
.cover__body{position:absolute;left:0;right:0;top:278px;bottom:38px;background:var(--blue);padding:14px 22px 0}
.cover__body h1{font-family:"Exo 2",sans-serif;font-weight:600;font-size:24px;line-height:1.05;color:#e8f6fc;margin-bottom:14px}
.cover__body h1 small{font-size:11px;font-weight:700}
.cover__body p{color:var(--white);font-size:8.8px;line-height:1.3}
.nas-art{position:absolute;right:16px;bottom:48px;width:140px;height:110px;background:linear-gradient(135deg,#cfe7f4,#5a7fa8);border-radius:6px}
</style>
</head>
<body>

<section class="spread spread--outside">
  <article class="panel">
    <div class="section">
      <h2>Geräte-Überwachung</h2>
      <p>Es gibt oft Geräte oder Systeme (Geländeüberwachung, Prozess-wichtige Drucker und Spezialgeräte), deren Ausfall hohe Kostenfolge oder sonstige negative Auswirkungen haben.</p>
      <p>Wir analysieren diese Systeme und definieren klare Alarme mit Alarmbedingungen. Aufgrund dieser Alarme legen wir ein Szenario fest, um die Fehler zu beheben und die Ursachen zu finden.<br>So stellen wir sicher, dass die Systeme rasch möglichst wieder einsatzbereit sind.<br>Ziehen diese Sofortmassnahmen nicht, wird das weitere Vorgehen mit Ihnen abgesprochen.<br>Erhöhen Sie die Integrität Ihrer wichtigen Systeme ab nur CHF 0.33(zzgl. MwSt) pro Tag</p>
    </div>
    <div class="section">
      <h2>Helpdesk-Agent</h2>
      <p>Mit unserem Helpdesk-Agent erhalten Sie einfacher Zugriff auf unser Ticket-System.<br>Somit haben Sie nebst den aktuellen Tickets auch vergangene Tickets im Blick.<br>So haben Sie stehts auch den Überblick, wie häufig etwas vorkommt oder wann die letzte Wartung durchgeführt wurde.<br>Den Helpdesk-Agent erhalten Sie bei Server-Wartungspaketen oder als eigenständiges Paket</p>
    </div>
    <div class="panel__footer"><span class="footer-url">www.rechnerhannes.ch</span></div>
  </article>

  <article class="panel">
    <div class="section">
      <h2>PassHafen</h2>
      <p>Wer kennt es nicht? Zahllose Passwörter und kein Überblick, oder die Listen sind nicht korrekt nachgeführt.<br>Für unsere Firmenkunde, bei welchen wir die Infrastruktur stellen, bieten wir die Möglichkeit, einen Zugriff auf unseren Passwort-Speicher zu mieten und so einen gemeinsamen Passwortspeicher zu pflegen.<br>So erhalten Sie immer die benötigten Passwörter, ohne lange am Telefon zu sein. Sicher und mit den aktuellsten Technologien geschützt.</p>
    </div>
    <div class="section">
      <h2>2-FA by Vireo Guard</h2>
      <p>In der heutigen Zeit ist eine Basisauthentifizierung mit Benutzername und Passwort längst kein zuverlässiger Schutz mehr.<br>„Zero Trust“, also 0 Vertrauen das Schlagwort der Stunde.<br>Sichern Sie Ihre wichtige IT-Infrastruktur schnell und einfach mit einer zusätzlichen Authentifizierungslösung von Vireo Guard.<br>Vireo Guard gehört zu Korvex Networks, einem der grössten Player im Bereich Zugriffsschutz.<br>Sichern Sie Ihre Computer, Server und Webseiten-Administrationsoberflächen mit einer 2. Authentifizierung, wir unterstützen und beraten Sie gerne dabei.</p>
    </div>
    <div class="panel__footer"></div>
    <div class="contact">
      <h3>Kontakt</h3>
      <div class="contact__cols">
        <div>rechnerhannes.ch GmbH<br>9347 Lindenmatt<br>+ 8612 Tannegg</div>
        <div>Telefon: 071 483 27 96<br>E-Mail: info@rechnerhannes.ch<br>Web: rechnerhannes.ch</div>
      </div>
    </div>
  </article>

  <article class="panel panel--cover">
    <div class="cover__portrait" role="img" aria-label="Gezeichnetes Porträt eines bärtigen Philosophen in Rot und Blau"></div>
    <div class="brand">
      <span class="brand__mark"></span>
      <span class="brand__name">RECHNER<br>HANNES</span>
    </div>
    <div class="brand__tagline">Swift Relay</div>
    <svg class="cover__swoosh" viewBox="0 0 380 120" preserveAspectRatio="none" aria-hidden="true">
      <path d="M0 88 Q200 135 380 18 L380 120 L0 120Z" fill="#1fa6dc"/>
      <path d="M0 70 Q200 120 380 2 L380 20 Q200 138 0 90Z" fill="#a5181d"/>
      <path d="M0 64 Q200 112 380 -4 L380 4 Q200 122 0 72Z" fill="#1fa6dc"/>
    </svg>
    <div class="cover__body">
      <h1>Das einzige Beständige<br>ist die Veränderung <small>(Arkadios)</small></h1>
      <p>In der heutigen Zeit verändert sich die Anforderungen an die IT und deren Verfügbarkeit und Sicherheit in einem rasanten Tempo.<br>Um dieser Tatsache gerecht zu werden, haben wir unser Serviceangebot überarbeitet. So erfahren Sie alles zu unseren Service-dienstleistungen auf den folgenden Seiten.<br>Unsere Servicedienstleistungspakete sind modular aufgebaut und können so als Gesamtpaket Ihren Bedürfnissen entsprechend zusammengestellt werden.<br>Zudem versuchen wir Ihnen auch das Erlangen von zeitnaher und zielgerichteter Hilfe mit unserem Helpdesk-Agenten zu erleichtern.</p>
    </div>
    <div class="panel__footer"><span class="footer-url">www.rechnerhannes.ch</span></div>
  </article>
</section>

<section class="spread spread--inside">
  <article class="panel panel--shade">
    <h2>Firewall-Unterhalt</h2>
    <p class="lead">Die Firewall ist ein wichtiger Bestandteil beim Schutz Ihres Firmennetzwerkes, denn sie ist das Eingangstor in Ihr Unternehmen.</p>
    <p class="lead">Um ihrer Schutzfunktion gerecht werden zu können, sind einige Punkte zu beachten, wie zum Beispiel:</p>
    <ul>
      <li>Korrekte Konfiguration bei der Einrichtung</li>
      <li>Zugriffe von Ausserhalb klar definieren und wo immer möglich eng einschränken</li>
      <li>Vermeiden von Standard-Ports für Zugriffe von Aussen</li>
      <li>Starke und sichere Passwörter (min. 8 Zeichen, Gross-/Kleinschreibung, Zahlen und Sonderzeichen, keine Wörterbuchzeichenfolgen)</li>
      <li>Regelmässige Aktualisierungen der Firewall-Firmware</li>
    </ul>
    <p class="lead">Die häufigsten Ursachen für gehackte Firewalls sind:</p>
    <ul>
      <li>Einfache Passwörter wie Hallo123!</li>
      <li>Verwenden von Standard-Einstellungen bei Ports und Zugriffsbeschränkungen</li>
      <li>Veraltete Firmware, deren Sicherheitslücken ausgenutzt werden</li>
    </ul>
    <div class="infobox">
      <p class="lead">Mit unserer Firewall-Wartung wird Ihre Firewall 4 mal im Jahr von uns geprüft und bei Bedarf aktualisiert. Ebenso werden die wichtigsten Indikatoren für Angriffe permanent durch unser Alarmsystem überwacht.<br>Zudem setzten wir zu diesen Zeitpunkten sicherheitsrelevante Empfehlungen des Herstellers um.</p>
    </div>
    <div class="panel__footer"><span class="footer-url">www.rechnerhannes.ch</span></div>
  </article>

  <article class="panel panel--shade">
    <h2>Server-Unterhalt</h2>
    <p class="lead">Server sind in einem Firmennetzwerk die Zentrale Ihres Unternehmen.<br>Meist laufen darauf betriebswichtige Applikationen.<br>Sie sind daher auch das Hauptziel von gezielten Angriffen gegen das Unternehmen.<br>Zudem bietet ein Server, sei es in der Cloud oder vor Ort, aufgrund seiner Komplexität und Wartungsbedürfnissen eine enorme Angriffsfläche, welche durch folgende Faktoren einen erfolgreichen Angriff begünstigen:</p>
    <ul>
      <li>Schwache Passwörter (Hallo123!)</li>
      <li>Schlechter Wartungsstand bei den Updates</li>
      <li>Vernachlässigter oder fehlender Virenschutz</li>
    </ul>
    <div class="infobox">
      <p class="lead">Nebst unseren weiteren Produkten in den Bereichen Virenschutz und Datensicherung bieten unsere Server-Wartungsverträge Ihnen folgende Vorteile:</p>
      <ul>
        <li>Ein, Ihrem Zyklus entsprechend aktuell gehaltenes System</li>
        <li>Permanentes Monitoring kritischer Werte, wie Verfügbarkeit, Temperatur, Speicherauslastung und Festplattennutzung</li>
        <li>Transparenter Support dank Ticket-System und klar definierten Alarm-Aktionen</li>
        <li>1 Helpdesk Agent für einen schnellen und komfortablen Zugriff auf das Ticket-System</li>
      </ul>
    </div>
    <div class="panel__footer"><span class="footer-slogan">WIR HABEN DIE LÖSUNG</span></div>
  </article>

  <article class="panel panel--shade">
    <h2>NAS-Unterhalt</h2>
    <p class="lead">Wie Server sind auch NAS in Ihrer Funktion als zentraler Datenablageort wichtig für Ihr Unternehmen.<br>Daher ist eine Pflege und Überwachung dieser Geräte für eine hohe Verfügbarkeit unerlässlich.<br>Den auch ein NAS birgt Gefahren für Ihr Unternehmen:</p>
    <ul>
      <li>Datendiebstahl durch Ausnutzung von Sicherheitslücken und schwachen Passwörtern</li>
      <li>Datenverlust durch Hardwareschäden und-Ausfällen</li>
      <li>Verschlüsselungstrojaner</li>
    </ul>
    <div class="infobox">
      <p class="lead">Unsere Wartungsverträge helfen Ihnen die Sicherheit und Verfügbarkeit Ihrer NAS zu erhöhen:</p>
      <ul>
        <li>Stehts dem gewählten Intervall entsprechend aktualisierte Firmware</li>
        <li>Überwachung von Gerätegesundheit und Betriebsparameter durch Mail-Alarmierung an uns</li>
        <li>Sicherheitsrelevante Empfehlungen unserer geschulten Mitarbeitern</li>
      </ul>
    </div>
    <div class="nas-art" role="img" aria-label="Isometrische Illustration von Servern, Laptop und Cloud"></div>
    <div class="panel__footer"><span class="footer-url">www.rechnerhannes.ch</span></div>
  </article>
</section>

</body>
</html>
```